Gelato Business Card

create a new business card using existing logo

Target Market(s)

B2B

Contact Information for Business Card

typical contact info: logo, address, email, phone, rep name

Colors
0355a3
33a6d7

Requirements
Must have
• a feel of high quality, luxury, happiness
• use cool, comforting color and texture of business card.
Nice to have
• "A Little Perfection Goes A Long Way!" TM
• or, "more quality, more flavor"
• or, "Flavor Matters"

```html
<!DOCTYPE html>
<html lang="en">
<head>
<meta charset="utf-8">
<title>Marvella's Business Card</title>
<link href="https://fonts.googleapis.com/css2?family=Montserrat:wght@400;500;600&display=swap" rel="stylesheet">
<style>
  :root {
    --backdrop: #2b2b2d;
    --card: #ffffff;
    --brand-blue: #3452a3;
    --brand-sky: #33a6d7;
    --cone-orange: #e8775a;
    --cone-yellow: #eec21a;
    --name-yellow: #f2c21b;
    --text-grey: #4a4a4a;
  }
  * { margin: 0; padding: 0; box-sizing: border-box; }
  html, body {
    width: 1200px;
    height: 914px;
    overflow: hidden;
    background: var(--backdrop);
    font-family: "Montserrat", sans-serif;
  }
  .business-card {
    position: absolute;
    left: 365px;
    top: 47px;
    width: 469px;
    height: 820px;
    background: var(--card);
    overflow: hidden;
  }
  .brand {
    position: absolute;
    top: 92px;
    left: 0;
    width: 100%;
    display: flex;
    align-items: center;
    justify-content: center;
    gap: 12px;
  }
  .brand-dot {
    width: 18px;
    height: 18px;
    border-radius: 50%;
    background: var(--brand-blue);
  }
  .brand-name {
    font-size: 40px;
    font-weight: 600;
    color: var(--brand-blue);
    letter-spacing: 0.5px;
  }
  .gelato-swirl {
    position: absolute;
    left: 0;
    top: 215px;
    width: 300px;
    height: 320px;
    border-radius: 0 130px 130px 0;
    background: var(--brand-blue);
  }
  .waffle-cone {
    position: absolute;
    left: 0;
    top: 545px;
    width: 215px;
    height: 275px;
    background: linear-gradient(200deg, var(--cone-orange) 0%, var(--cone-yellow) 100%);
    clip-path: polygon(0 0, 100% 0, 100% 70%, 72% 100%, 0 100%);
  }
  .rep {
    position: absolute;
    left: 0;
    top: 428px;
    width: 300px;
    text-align: center;
  }
  .rep-name {
    font-size: 27px;
    font-weight: 600;
    color: var(--name-yellow);
    line-height: 1.15;
  }
  .rep-title {
    font-size: 22px;
    font-weight: 400;
    color: #ffffff;
    line-height: 1.2;
  }
  .contact {
    position: absolute;
    right: 22px;
    top: 580px;
    text-align: right;
    color: var(--text-grey);
    font-size: 14px;
    line-height: 1.55;
  }
  .address { margin-bottom: 24px; padding-right: 27px; }
  .contact-line {
    display: flex;
    justify-content: flex-end;
    align-items: center;
    gap: 10px;
  }
  .contact-icon {
    width: 17px;
    height: 17px;
    flex: none;
  }
</style>
</head>
<body>
  <div class="business-card">
    <div class="brand">
      <span class="brand-dot"></span>
      <span class="brand-name">Marvella's</span>
    </div>

    <div class="gelato-swirl" role="img" aria-label="Illustration of a blue swirled scoop of gelato"></div>
    <div class="waffle-cone" role="img" aria-label="Illustration of an orange and yellow waffle cone"></div>

    <div class="rep">
      <p class="rep-name">John Doe</p>
      <p class="rep-title">Manager</p>
    </div>

    <div class="contact">
      <p class="address">123 Main Street<br>Anytown, AB, A1A 1A1</p>
      <p class="contact-line">123-456-7899
        <svg class="contact-icon" viewBox="0 0 24 24" aria-hidden="true"><path fill="var(--brand-blue)" d="M6.6 10.8a15 15 0 0 0 6.6 6.6l2.2-2.2a1 1 0 0 1 1-.25 11.4 11.4 0 0 0 3.6.57 1 1 0 0 1 1 1V20a1 1 0 0 1-1 1A17 17 0 0 1 3 4a1 1 0 0 1 1-1h3.5a1 1 0 0 1 1 1c0 1.250.2 2.45.57 3.6a1 1 0 0 1-.25 1z"/></svg>
      </p>
      <p class="contact-line">john.doe@marvellas.com
        <svg class="contact-icon" viewBox="0 0 24 24" aria-hidden="true"><rect x="2" y="5" width="20" height="14" rx="1.5" fill="var(--brand-blue)"/><path d="M3 6.5l9 6.5 9-6.5" fill="none" stroke="#fff" stroke-width="1.6"/></svg>
      </p>
      <p class="contact-line">www.marvellas.com
        <svg class="contact-icon" viewBox="0 0 24 24" aria-hidden="true"><circle cx="12" cy="12" r="10" fill="var(--brand-blue)"/><g fill="none" stroke="#fff" stroke-width="1.3"><ellipse cx="12" cy="12" rx="4.5" ry="10"/><path d="M2 12h20M4 7h16M4 17h16M12 2v20"/></g></svg>
      </p>
    </div>
  </div>
</body>
</html>
```